Collectible Card Trading Company ~ Tidewell and Finch Collectibles

Business card design using the attached images as a reference point. The color pallet is the color choice I prefer. If you have any way of improving on the design that would be appreciated. This will be used as an insert for product shipments as well as at geekfair and other collectible trade shows so it needs to be eye catching and memorable. Anything that you can do to make my business POP with this business card would be appreciated.

Target Market(s)

Collectible card purchasers primarily but all collectors ingeneral

Industry/Entity Type

Retail

Contact Information for Business Card

Details are included on the provided images

Colors

Designer to choose colors to be used in the design.

Requirements
Must have
• Bold design
Nice to have
• N/A
Should not have
• N/A

```html
<!DOCTYPE html>
<html lang="en">
<head>
<meta charset="utf-8">
<title>Tidewell &amp; Finch Co. — Business Card</title>
<link rel="stylesheet" href="https://fonts.googleapis.com/css2?family=Barlow+Semi+Condensed:wght@700&family=Montserrat:wght@300;500&display=swap">
<style>
  :root {
    --backdrop: #eeeff1;
    --paper: #f5f5f4;
    --brass: #bf7a2c;
    --navy: #262b3a;
    --ink: #262b3a;
  }
  * { margin: 0; padding: 0; box-sizing: border-box; }
  html, body { width: 1200px; height: 900px; overflow: hidden; background: var(--backdrop); }
  .stage { position: relative; width: 1200px; height: 900px; }

  .card {
    position: absolute;
    top: 235px;
    width: 276px;
    height: 429px;
    background: var(--paper);
  }
  .card--front { left: 266px; }
  .card--back { left: 642px; }
  .card__art { position: absolute; inset: 0; }

  .brand-name {
    font-family: "Barlow Semi Condensed", sans-serif;
    font-weight: 700;
    fill: var(--brass);
  }

  .identity {
    position: absolute;
    left: 47px;
    top: 267px;
    color: var(--brass);
  }
  .identity__name {
    font-family: "Barlow Semi Condensed", sans-serif;
    font-weight: 700;
    font-size: 21px;
    line-height: 20px;
    letter-spacing: 0.3px;
  }
  .identity__title {
    font-family: "Montserrat", sans-serif;
    font-weight: 300;
    font-size: 14.5px;
    line-height: 17px;
    letter-spacing: 0.2px;
  }

  .contacts {
    position: absolute;
    left: 47px;
    top: 323px;
    list-style: none;
  }
  .contacts__item {
    display: flex;
    align-items: center;
    height: 20.3px;
    font-family: "Montserrat", sans-serif;
    font-weight: 500;
    font-size: 11.6px;
    color: var(--ink);
  }
  .contacts__icon {
    width: 13px;
    height: 13px;
    margin-right: 7px;
    flex: none;
  }
</style>
</head>
<body>
<main class="stage">

  <!-- Front of card -->
  <section class="card card--front" aria-label="Card front">
    <svg class="card__art" viewBox="0 0 276 429" width="276" height="429">
      <path d="M15 12 H260 V224.5 A122.5 122.5 0 0 1 15 224.5 Z" fill="var(--brass)"/>
      <circle cx="138" cy="224" r="104" fill="var(--navy)"/>
      <text class="brand-name" x="138" y="231" text-anchor="middle" font-size="20">Tidewell &amp; Finch Co.</text>
    </svg>
  </section>

  <!-- Back of card -->
  <section class="card card--back" aria-label="Card back">
    <svg class="card__art" viewBox="0 0 276 429" width="276" height="429">
      <path d="M20 12 H256 V128 A118 118 0 0 1 20 128 Z" fill="var(--brass)"/>
      <circle cx="138" cy="127.5" r="100" fill="var(--navy)"/>
      <text class="brand-name" x="138" y="134" text-anchor="middle" font-size="19">Tidewell &amp; Finch Co.</text>
    </svg>

    <div class="identity">
      <p class="identity__name">MARCUS HALE JR.</p>
      <p class="identity__title">CHIEF COLLECTOR</p>
    </div>

    <ul class="contacts">
      <li class="contacts__item">
        <svg class="contacts__icon" viewBox="0 0 13 13"><circle cx="6.5" cy="6.5" r="6.5" fill="var(--brass)"/></svg>
        tidewellfinchco
      </li>
      <li class="contacts__item">
        <svg class="contacts__icon" viewBox="0 0 13 13"><circle cx="6.5" cy="6.5" r="6.5" fill="var(--brass)"/></svg>
        Tidewell_Finch
      </li>
      <li class="contacts__item">
        <svg class="contacts__icon" viewBox="0 0 13 13">
          <circle cx="6.5" cy="6.5" r="6.5" fill="var(--brass)"/>
          <rect x="3.3" y="4.3" width="6.4" height="4.6" rx="0.6" fill="none" stroke="var(--paper)" stroke-width="0.9"/>
          <path d="M3.5 4.6 L6.5 6.9 L9.5 4.6" fill="none" stroke="var(--paper)" stroke-width="0.9"/>
        </svg>
        marcus@tidewellfinchco.com
      </li>
      <li class="contacts__item">
        <svg class="contacts__icon" viewBox="0 0 13 13">
          <circle cx="6.5" cy="6.5" r="6.5" fill="var(--brass)"/>
          <circle cx="6.5" cy="6.5" r="3.6" fill="none" stroke="var(--paper)" stroke-width="0.8"/>
          <ellipse cx="6.5" cy="6.5" rx="1.6" ry="3.6" fill="none" stroke="var(--paper)" stroke-width="0.8"/>
          <path d="M2.9 6.5 H10.1" stroke="var(--paper)" stroke-width="0.8"/>
        </svg>
        www.tidewellfinchco.com
      </li>
    </ul>
  </section>

</main>
</body>
</html>
```